Lorvena Aesthetic Doctor

I require an elegant, luxurious looking business card for my aesthetic business. I am a doctor and that will set me aside from competitors. I am planning to provide home and spa based treatments to clients with high expectations. I have attached my logo.

```html
<!DOCTYPE html>
<html lang="en">
<head>
<meta charset="utf-8">
<title>Lorvena Aesthetic Doctor – Business Card</title>
<link rel="stylesheet" href="https://fonts.googleapis.com/css2?family=Cormorant+Garamond:wght@400;500&family=Playfair+Display:wght@600&family=Quicksand:wght@400;500&family=Roboto+Condensed:wght@300;400&display=swap">
<style>
  :root {
    --bg: #e6e7e9;
    --paper: #ffffff;
    --grey: #9fa2a5;
    --grey-dark: #7c7f83;
    --grey-text: #8e9195;
    --blue: #16a3e6;
    --blue-deep: #1f6fb8;
    --blue-light: #8fd0f0;
    --rule: #a7a9ac;
  }
  * { margin: 0; padding: 0; box-sizing: border-box; }
  html, body { width: 1200px; height: 965px; overflow: hidden; }
  body {
    background: var(--bg);
    display: flex;
    flex-direction: column;
    align-items: center;
    justify-content: center;
    gap: 36px;
  }
  .card {
    position: relative;
    width: 760px;
    height: 434px;
    background: var(--paper);
    overflow: hidden;
    box-shadow: 0 6px 18px rgba(0,0,0,.12);
  }

  /* Front */
  .front-brand {
    position: absolute;
    left: 0; right: 0;
    top: 100px;
    display: flex;
    align-items: center;
    justify-content: center;
    gap: 18px;
  }
  .logo-mark {
    width: 150px;
    height: 136px;
    position: relative;
    flex: none;
  }
  .logo-mark .ring { position: absolute; inset: 0; }
  .logo-mark .art {
    position: absolute;
    left: 0; top: 28px;
    width: 124px; height: 82px;
    border-radius: 60% 40% 45% 55%;
    background: linear-gradient(100deg, var(--blue-light), var(--blue) 60%, var(--blue-deep));
    opacity: .9;
  }
  .wordmark { color: var(--grey); }
  .wordmark .name {
    font-family: "Cormorant Garamond", serif;
    font-weight: 400;
    font-size: 72px;
    letter-spacing: 5px;
    line-height: .9;
  }
  .wordmark .tag {
    font-family: "Cormorant Garamond", serif;
    font-weight: 500;
    font-size: 27px;
    letter-spacing: 2.5px;
    line-height: 1;
    color: var(--grey-dark);
  }
  .tagline-row {
    position: absolute;
    left: 40px; right: 40px;
    top: 330px;
    display: flex;
    align-items: center;
    gap: 18px;
  }
  .tagline-row .rule { flex: 1; height: 1.5px; background: var(--rule); }
  .tagline-row .text {
    font-family: "Cormorant Garamond", serif;
    font-weight: 500;
    font-size: 20px;
    letter-spacing: 2px;
    color: var(--blue);
    text-transform: uppercase;
  }

  /* Back */
  .back-disc {
    position: absolute;
    left: 430px; top: -110px;
    width: 450px; height: 450px;
  }
  .back-disc .art {
    position: absolute;
    left: 70px; top: 150px;
    width: 230px; height: 145px;
    border-radius: 55% 45% 40% 60%;
    background: linear-gradient(100deg, var(--blue-light), var(--blue) 55%, var(--blue-deep));
  }
  .back-info {
    position: absolute;
    left: 44px; top: 40px;
  }
  .back-info .brand-name {
    font-family: "Cormorant Garamond", serif;
    font-size: 56px;
    letter-spacing: 4px;
    line-height: .9;
    color: var(--grey);
  }
  .back-info .brand-tag {
    font-family: "Cormorant Garamond", serif;
    font-weight: 500;
    font-size: 23px;
    letter-spacing: 2px;
    line-height: 1.1;
    color: var(--blue);
  }
  .person { margin-top: 18px; }
  .person .line { display: flex; align-items: baseline; gap: 10px; }
  .person .doctor {
    font-family: "Playfair Display", serif;
    font-weight: 600;
    font-size: 28px;
    line-height: 1.2;
    color: var(--blue);
  }
  .person .letters {
    font-family: "Roboto Condensed", sans-serif;
    font-size: 15px;
    color: var(--grey-text);
    border-left: 2px solid var(--grey-dark);
    padding-left: 9px;
  }
  .person .diploma {
    font-family: "Roboto Condensed", sans-serif;
    font-weight: 300;
    font-size: 17px;
    color: var(--grey-text);
  }
  .contacts { margin-top: 16px; list-style: none; }
  .contacts li {
    display: flex; align-items: center; gap: 12px;
    font-family: "Quicksand", sans-serif;
    font-size: 19px;
    color: var(--grey-text);
    line-height: 1.4;
  }
  .contacts svg { width: 17px; height: 17px; flex: none; }
  .contacts .hl { color: var(--blue); font-weight: 500; }
  .socials {
    position: absolute;
    left: 440px; top: 292px;
    display: flex; gap: 12px;
  }
  .socials span {
    width: 22px; height: 22px; border-radius: 50%;
    background: var(--blue);
  }
  .services {
    position: absolute;
    left: 44px; top: 326px;
    font-family: "Roboto Condensed", sans-serif;
    font-weight: 300;
    font-size: 17px;
    line-height: 1.3;
    color: var(--grey-text);
  }
</style>
</head>
<body>

  <section class="card card-front" aria-label="Card front">
    <div class="front-brand">
      <div class="logo-mark">
        <div class="art" role="img" aria-label="Brand mark: flowing blue hair emblem"></div>
        <svg class="ring" viewBox="0 0 150 136" aria-hidden="true">
          <path d="M56 9 A64 64 0 1 1 48 128" fill="none" stroke="var(--grey)" stroke-width="4"/>
        </svg>
      </div>
      <div class="wordmark">
        <div class="name">LORVENA</div>
        <div class="tag">AESTHETIC DOCTOR</div>
      </div>
    </div>
    <div class="tagline-row">
      <span class="rule"></span>
      <span class="text">Home and Spa Based Treatments</span>
      <span class="rule"></span>
    </div>
  </section>

  <section class="card card-back" aria-label="Card back">
    <div class="back-disc">
      <svg viewBox="0 0 450 450" width="450" height="450" aria-hidden="true">
        <circle cx="225" cy="225" r="222" fill="var(--blue)"/>
        <circle cx="232" cy="214" r="214" fill="var(--grey)"/>
        <path d="M150 95 A150 150 0 1 1 180 380" fill="none" stroke="#fff" stroke-width="4"/>
      </svg>
      <div class="art" role="img" aria-label="Large brand emblem: flowing blue hair"></div>
    </div>

    <div class="back-info">
      <div class="brand-name">LORVENA</div>
      <div class="brand-tag">AESTHETIC DOCTOR</div>

      <div class="person">
        <div class="line">
          <span class="doctor">Dr Mireille Vostan</span>
          <span class="letters">MRCPCH MD</span>
        </div>
        <div class="diploma">Australasian Diploma of Aesthetic Medicine</div>
      </div>

      <ul class="contacts">
        <li>
          <svg viewBox="0 0 24 24" fill="none" stroke="var(--blue)" stroke-width="2"><path d="M5 3h4l2 5-3 2a11 11 0 0 0 6 6l2-3 5 2v4a2 2 0 0 1-2 2A17 17 0 0 1 3 5a2 2 0 0 1 2-2z"/></svg>
          0800 555 014
        </li>
        <li>
          <svg viewBox="0 0 24 24" fill="none" stroke="var(--blue)" stroke-width="2"><rect x="3" y="5" width="18" height="14" rx="1"/><path d="M3 6l9 7 9-7"/></svg>
          mireille@lorvena.co.nz
        </li>
        <li>
          <svg viewBox="0 0 24 24" fill="none" stroke="var(--blue)" stroke-width="2"><circle cx="12" cy="12" r="9"/><path d="M3 12h18M12 3c3 3 3 15 0 18M12 3c-3 3-3 15 0 18"/></svg>
          <span>www.<span class="hl">lorvena</span>.co.nz</span>
        </li>
      </ul>
    </div>

    <div class="socials" aria-hidden="true"><span></span><span></span></div>

    <p class="services">
      Dermal injectables - Plasma facials - Microneedling<br>
      Skin boosters - Excessive sweating<br>
      Home and Spa Based Treatments
    </p>
  </section>

</body>
</html>
```